Real Estate Website

We have a an existing website - harborkeyhomes.com.au which we want redesigned.

We want it to look more like the design/style of https://www.stallworth.com.au/

```html
<!DOCTYPE html>
<html lang="en">
<head>
<meta charset="utf-8">
<title>Harborkey Estate Agents</title>
<link rel="stylesheet" href="https://fonts.googleapis.com/css2?family=Poppins:wght@300;400;500;600&family=Roboto+Condensed:wght@700&display=swap">
<style>
:root{
  --teal:#009a9a;
  --teal-dark:#008585;
  --black:#000;
  --ink:#1a1a1a;
  --text:#444;
  --grey-bg:#efefef;
  --white:#fff;
  --dark:#1f1f1f;
}
*{box-sizing:border-box;margin:0;padding:0}
html,body{width:1200px;height:4216px;overflow:hidden}
body{position:relative;font-family:"Poppins",sans-serif;color:var(--text);background:var(--white)}
.abs{position:absolute}
.heading{font-family:"Roboto Condensed",sans-serif;font-weight:700;color:var(--ink);font-size:30px;line-height:1.2;display:flex;align-items:center;gap:14px;white-space:nowrap}
.heading .rule{display:inline-block;width:50px;height:6px;border-top:1.5px solid var(--teal);border-bottom:1.5px solid var(--teal)}
.heading.light{color:var(--white)}
.heading.light .rule{border-color:var(--white)}
.heading.center{justify-content:center;left:0;width:1200px}
.photo{position:absolute}

/* top bar */
.topbar{left:0;top:0;width:1200px;height:36px;background:var(--black);color:var(--white);font-size:12px}
.topbar .welcome{position:absolute;left:60px;top:10px}
.social{position:absolute;display:flex;gap:8px}
.social span{width:24px;height:24px;border:1.5px solid var(--white);border-radius:50%}

/* header */
.brand{left:60px;top:58px;display:flex;align-items:center;gap:12px}
.brand .mark{width:22px;height:22px;background:var(--teal)}
.brand .name{font-size:30px;font-weight:400;letter-spacing:3px;color:var(--ink);line-height:1.2}
.contact-item{display:flex;gap:14px;font-size:12px;color:var(--ink);line-height:1.6}
.contact-item .label{font-weight:500}
.contact-item .val{color:#555}
.contact-item svg{flex:none}

.nav{left:165px;top:123px;width:708px;height:52px;background:var(--black);display:flex;align-items:center;padding-left:76px;font-size:12px;color:var(--white)}
.nav a{color:var(--white);text-decoration:none;margin-right:58px}
.nav a.active{color:var(--teal)}
.btn-contact{left:899px;top:123px;width:136px;height:52px;background:var(--teal);color:var(--white);font-weight:600;font-size:14px;display:flex;align-items:center;justify-content:center}

/* hero */
.hero{left:0;top:123px;width:1200px;height:638px;background:linear-gradient(120deg,#3a3228 0%,#8a7a62 45%,#cfc6b6 70%,#6d6250 100%)}
.hero-title{left:60px;top:370px;font-size:84px;line-height:1;font-weight:400;color:var(--white);letter-spacing:2px;white-space:nowrap}
.hero-text{left:60px;top:466px;width:420px;font-size:12px;line-height:1.7;color:var(--white)}
.btn{display:flex;align-items:center;justify-content:center;font-weight:600;font-size:14px;color:var(--white)}
.hero-btn{left:60px;top:529px;width:135px;height:36px;background:var(--teal)}

/* about */
.about-text{left:60px;top:882px;width:485px;font-size:12px;line-height:1.65}
.thumb{top:989px;width:158px;height:195px;background:linear-gradient(160deg,#f4f2ee,#d6d2ca)}

/* who */
.who{left:0;top:1347px;width:1200px;height:367px;background:var(--grey-bg)}
.who-card{top:1463px;width:209px;height:164px;background:var(--white);display:flex;flex-direction:column;align-items:center;font-size:15px;color:var(--ink)}
.who-card svg{margin-top:28px;margin-bottom:30px}

/* news */
.news{left:0;top:1714px;width:1200px;height:593px;background:var(--teal)}
.news-cap{top:2194px;font-size:15px;color:var(--white);text-align:center;white-space:nowrap}
.news-date{top:2223px;font-size:11px;color:var(--white);text-align:center;white-space:nowrap}

/* testimonials */
.testi-text{left:60px;top:2436px;width:450px;font-size:12px;line-height:1.65}
.testi-sign{left:60px;top:2607px;font-size:15px;color:var(--teal)}
.ring{left:758px;top:2387px;width:344px;height:344px;border-radius:50%;background:#111;display:flex;align-items:center;justify-content:center}
.ring div{width:284px;height:284px;border-radius:50%;background:radial-gradient(circle at 50% 45%,#d8d8d8,#8a8a8a)}

/* agents */
.agents-bg{left:0;top:2806px;width:1200px;height:345px;background:linear-gradient(90deg,#141414,#3a3a3a 50%,#141414)}
.agent-photo{top:2957px;width:225px;height:239px}
.agent-bracket{top:3196px;height:16px;border:5px solid var(--teal);border-top:none}
.agent-name{top:3226px;font-size:15px;color:var(--ink);text-align:center}
.agent-role{top:3252px;font-size:12px;color:var(--teal);text-align:center}

/* listings */
.listing{top:3385px;width:308px;height:361px;background:var(--white);box-shadow:0 2px 14px rgba(0,0,0,.08)}
.listing .img{height:210px;background:linear-gradient(180deg,#b9c9d6,#e9e7e1 55%,#6c8a4c)}
.listing .loc{display:flex;gap:10px;padding:22px 0 0 28px;font-size:12px;line-height:1.65;color:#555}
.listing .btn{position:absolute;top:297px;left:50%;transform:translateX(-50%);width:136px;height:36px}

/* footer */
.footer{left:0;top:3817px;width:1200px;height:364px;background:var(--teal);color:var(--white)}
.footer h4{font-size:17px;font-weight:600;margin-bottom:16px}
.footer ul{list-style:none;font-size:12px;line-height:22.5px}
.f-col{position:absolute;top:70px}
.f-brand{position:absolute;left:60px;top:76px;font-size:28px;line-height:1.2;letter-spacing:3px;display:flex;align-items:center;gap:12px}
.f-brand i{display:block;width:18px;height:18px;background:var(--white)}
.f-info{position:absolute;left:60px;display:flex;gap:16px;font-size:12px;line-height:1.6;width:250px}
.bottombar{left:0;top:4181px;width:1200px;height:35px;background:var(--black);color:var(--white);font-size:12px}
</style>
</head>
<body>

<!-- top bar -->
<div class="abs topbar">
  <span class="welcome">Welcome To Harborkey Estate Agents !</span>
  <div class="social" style="left:1080px;top:6px"><span></span><span></span></div>
</div>

<!-- header -->
<div class="abs brand"><span class="mark"></span><span class="name">HARBORKEY</span></div>
<div class="abs contact-item" style="left:605px;top:52px">
  <svg width="36" height="36" viewBox="0 0 36 36"><circle cx="18" cy="18" r="16" fill="none" stroke="#009a9a" stroke-width="1.5"/><path d="M18 9a6 6 0 0 0-6 6c0 5 6 11 6 11s6-6 6-11a6 6 0 0 0-6-6z" fill="none" stroke="#009a9a" stroke-width="1.5"/><circle cx="18" cy="15" r="2" fill="#009a9a"/></svg>
  <div><div class="label">Email</div><div class="val">enquiries@harborkeyhomes.com.au</div></div>
</div>
<div class="abs contact-item" style="left:905px;top:52px">
  <svg width="36" height="36" viewBox="0 0 36 36"><circle cx="18" cy="18" r="16" fill="none" stroke="#009a9a" stroke-width="1.5"/><rect x="10" y="12" width="16" height="12" rx="1" fill="none" stroke="#009a9a" stroke-width="1.5"/><path d="M10 13l8 6 8-6" fill="none" stroke="#009a9a" stroke-width="1.5"/></svg>
  <div style="width:180px"><div class="label">Location</div><div class="val">Shop 4, 27 Quay Rd, Botany NSW 2019</div></div>
</div>

<!-- hero -->
<div class="abs hero" role="img" aria-label="Photo of a young couple meeting a real estate agent in a bright living room"></div>
<nav class="abs nav">
  <a class="active">Home</a><a>Buying</a><a>Selling</a><a>Renting</a><a>Blog</a><a>About Us</a>
</nav>
<div class="abs btn-contact">CONTACT US</div>
<h1 class="abs hero-title">HARBORKEY</h1>
<p class="abs hero-text">Understanding clients and their personal struggles within the real estate industry is what we do best.</p>
<div class="abs btn hero-btn">LEARN MORE</div>

<!-- about -->
<h2 class="abs heading" style="left:60px;top:832px">About Us <span class="rule"></span></h2>
<p class="abs about-text">Harborkey Estate Agency is driven by a passionate, hardworking, caring team who are your friends in real estate. We are forward thinkers, digital innovators, who are 110% customer service focused and always looking at ways to raise the bar when it comes to property services and making our clients happy.</p>
<div class="abs thumb" style="left:60px" role="img" aria-label="Photo of a modern living room"></div>
<div class="abs thumb" style="left:232px" role="img" aria-label="Photo of a dining and kitchen area"></div>
<div class="abs thumb" style="left:404px" role="img" aria-label="Photo of a bathroom with shower"></div>
<div class="photo" style="left:701px;top:848px;width:435px;height:424px;background:linear-gradient(160deg,#c79a80,#a9735a 60%,#7a5240)" role="img" aria-label="Photo of an agent showing a couple around an empty room"></div>

<!-- who we are -->
<div class="abs who"></div>
<h2 class="abs heading center" style="top:1403px">Who We Are <span class="rule"></span></h2>
<div class="abs who-card" style="left:146px">
  <svg width="46" height="46" viewBox="0 0 46 46" fill="none" stroke="#009a9a" stroke-width="1.8"><path d="M4 22L23 5l19 17M9 18v23h28V18"/><path d="M23 17l7 3v5c0 5-3 8-7 10-4-2-7-5-7-10v-5z"/><path d="M23 23v4"/></svg>
  Property Alert</div>
<div class="abs who-card" style="left:378px">
  <svg width="46" height="46" viewBox="0 0 46 46" fill="none" stroke="#009a9a" stroke-width="1.8"><path d="M3 22L23 4l20 18M8 18v24h30V18"/><path d="M18 42V29h10v13"/></svg>
  Market Appraisal</div>
<div class="abs who-card" style="left:611px">
  <svg width="50" height="46" viewBox="0 0 50 46" fill="none" stroke="#009a9a" stroke-width="1.8"><circle cx="25" cy="12" r="6"/><circle cx="11" cy="16" r="5"/><circle cx="39" cy="16" r="5"/><path d="M15 40V30a10 10 0 0 1 20 0v10M3 38v-7a8 8 0 0 1 10-8M47 38v-7a8 8 0 0 0-10-8"/></svg>
  Our Team</div>
<div class="abs who-card" style="left:843px">
  <svg width="46" height="46" viewBox="0 0 46 46" fill="none" stroke="#009a9a" stroke-width="1.8"><path d="M5 20v22h36V20L23 32z"/><path d="M5 20l18 22 18-22"/><circle cx="23" cy="14" r="10"/><path d="M19 12c0 4 3 7 7 7l2-2-3-2-1 1c-1 0-3-2-3-3l1-1-2-3z"/></svg>
  Contact Us</div>

<!-- news -->
<div class="abs news"></div>
<h2 class="abs heading light center" style="top:1786px">News <span class="rule"></span></h2>
<div class="photo" style="left:0;top:1842px;width:283px;height:337px;background:linear-gradient(180deg,#b8cde0,#a55a3c 50%,#4c6a35)" role="img" aria-label="Photo of a red brick house with garden"></div>
<div class="photo" style="left:314px;top:1842px;width:570px;height:337px;background:linear-gradient(180deg,#5b9fe0,#a9cdee 45%,#7d8c6e 70%,#e5e5e5)" role="img" aria-label="Photo of a city skyline view from a balcony"></div>
<div class="photo" style="left:915px;top:1842px;width:285px;height:337px;background:linear-gradient(180deg,#e9e9e9,#cfcfcf 60%,#bdb7ae)" role="img" aria-label="Photo of a furnished bedroom"></div>
<div class="abs news-cap" style="left:-140px;width:423px">Sold by Clara Moretti 0400 111 222 - $670,000</div>
<div class="abs news-date" style="left:-22px;text-align:left">15 April,2021</div>
<div class="abs news-cap" style="left:314px;width:570px">Sold by Clara Moretti 0400 111 222 - $670,000</div>
<div class="abs news-date" style="left:314px;width:570px">15 April,2021</div>
<div class="abs news-cap" style="left:966px;text-align:left">Sold by Clara Moretti 0400 111 222</div>
<div class="abs news-date" style="left:1105px;text-align:left">15 April,2021</div>

<!-- testimonials -->
<h2 class="abs heading" style="left:60px;top:2385px">Testimonials <span class="rule"></span></h2>
<p class="abs testi-text">Lorem Ipsum is simply dummy text of the printing and typesetting industry. Lorem Ipsum has been the industry's standard dummy text ever since the 1500s, when an unknown printer took a galley of type and scrambled it to make a type specimen book. Lorem Ipsum is simply dummy text of the printing and typesetting industry. Lorem Ipsum has been the industry's standard dummy text ever since the 1500s, when an unknown printer took a galley of type and scrambled it to make a type specimen book.</p>
<div class="abs testi-sign">Dear Leo</div>
<div class="abs ring"><div role="img" aria-label="Portrait photo of the client giving the testimonial"></div></div>

<!-- agents -->
<div class="abs agents-bg" role="img" aria-label="Dark blurred office photo background"></div>
<h2 class="abs heading light center" style="top:2885px">Our Agents <span class="rule"></span></h2>

<div class="photo agent-photo" style="left:105px;background:linear-gradient(180deg,#9a8f86,#5d6472)" role="img" aria-label="Portrait photo of agent Leo Tran"></div>
<div class="abs agent-bracket" style="left:130px;width:180px"></div>
<div class="abs agent-name" style="left:105px;width:225px">Leo Tran</div>
<div class="abs agent-role" style="left:90px;width:235px">Director</div>

<div class="photo agent-photo" style="left:358px;background:linear-gradient(180deg,#8f8e8c,#2c3650)" role="img" aria-label="Portrait photo of agent Marcus Lee"></div>
<div class="abs agent-bracket" style="left:383px;width:180px"></div>
<div class="abs agent-name" style="left:358px;width:225px">Marcus Lee</div>
<div class="abs agent-role" style="left:368px;width:225px">Principal</div>

<div class="photo agent-photo" style="left:614px;background:linear-gradient(180deg,#7e9467,#2a2a2a)" role="img" aria-label="Portrait photo of agent Sofia Haddad"></div>
<div class="abs agent-bracket" style="left:639px;width:180px"></div>
<div class="abs agent-name" style="left:614px;width:225px">Sofia Haddad</div>
<div class="abs agent-role" style="left:622px;width:225px">Property Management</div>

<div class="photo agent-photo" style="left:869px;background:linear-gradient(180deg,#f3f3f3,#1d2233)" role="img" aria-label="Portrait photo of agent Clara Moretti"></div>
<div class="abs agent-bracket" style="left:894px;width:180px"></div>
<div class="abs agent-name" style="left:864px;width:225px">Clara Moretti</div>
<div class="abs agent-role" style="left:867px;width:225px">Director</div>

<!-- featured listings -->
<h2 class="abs heading center" style="top:3328px">Featured Listings <span class="rule"></span></h2>

<div class="abs listing" style="left:108px">
  <div class="img" role="img" aria-label="Photo of a white two-storey family home"></div>
  <div class="loc"><svg width="16" height="20" viewBox="0 0 16 20" fill="none" stroke="#009a9a" stroke-width="1.5"><path d="M8 1a6 6 0 0 0-6 6c0 5 6 11 6 11s6-6 6-11a6 6 0 0 0-6-6z"/><circle cx="8" cy="7" r="2"/></svg><span>Lorem Ipsum is dummy ptinting<br>type industry</span></div>
  <div class="btn" style="background:var(--black)">LEARN MORE</div>
</div>
<div class="abs listing" style="left:445px">
  <div class="img" role="img" aria-label="Photo of a modern white home at dusk"></div>
  <div class="loc"><svg width="16" height="20" viewBox="0 0 16 20" fill="none" stroke="#009a9a" stroke-width="1.5"><path d="M8 1a6 6 0 0 0-6 6c0 5 6 11 6 11s6-6 6-11a6 6 0 0 0-6-6z"/><circle cx="8" cy="7" r="2"/></svg><span>Lorem Ipsum is dummy ptinting<br>type industry</span></div>
  <div class="btn" style="background:var(--teal)">LEARN MORE</div>
</div>
<div class="abs listing" style="left:782px">
  <div class="img" style="background:linear-gradient(180deg,#e6e3dc,#b9ad93 55%,#4d5b3a)" role="img" aria-label="Photo of a home entrance with lit windows"></div>
  <div class="loc"><svg width="16" height="20" viewBox="0 0 16 20" fill="none" stroke="#009a9a" stroke-width="1.5"><path d="M8 1a6 6 0 0 0-6 6c0 5 6 11 6 11s6-6 6-11a6 6 0 0 0-6-6z"/><circle cx="8" cy="7" r="2"/></svg><span>Lorem Ipsum is dummy ptinting<br>type industry</span></div>
  <div class="btn" style="background:var(--black)">LEARN MORE</div>
</div>

<!-- footer -->
<footer class="abs footer">
  <div class="f-brand"><i></i>HARBORKEY</div>
  <div class="f-info" style="top:121px">
    <svg width="16" height="20" viewBox="0 0 16 20" fill="none" stroke="#fff" stroke-width="1.5"><path d="M8 1a6 6 0 0 0-6 6c0 5 6 11 6 11s6-6 6-11a6 6 0 0 0-6-6z"/><circle cx="8" cy="7" r="2"/></svg>
    <span>Shop 4, 27 Quay Rd, Botany NSW 2019</span></div>
  <div class="f-info" style="top:180px">
    <svg width="16" height="16" viewBox="0 0 16 16" fill="#fff"><path d="M3 1l3 3-2 2c1 2 3 4 5 5l2-2 3 3-2 3C7 15 1 9 0 4z"/></svg>
    <span>02 9000 1234</span></div>
  <div class="f-info" style="top:232px">
    <svg width="18" height="14" viewBox="0 0 18 14" fill="none" stroke="#fff" stroke-width="1.5"><rect x="1" y="1" width="16" height="12"/><path d="M1 1l8 7 8-7"/></svg>
    <span>enquiries@harborkeyhomes.com.au</span></div>

  <div class="f-col" style="left:337px"><h4>Buying</h4><ul>
    <li>- Properties for Sale</li><li>- Commercial for Sale</li><li>- Land for Sale</li><li>- Open Homes</li><li>- Auction Timetable</li><li>- Buying Tips</li><li>- Sales Team</li><li>- Property Alert</li></ul></div>
  <div class="f-col" style="left:614px"><h4>Selling</h4><ul>
    <li>- Selling Tips</li><li>- Market Appraisal</li><li>- Recent Sales</li><li>- Testimonials</li></ul></div>
  <div class="f-col" style="left:889px"><h4>Renting</h4><ul>
    <li>- Properties for Lease</li><li>- Commercial for Lease</li><li>- Rental Open Homes</li><li>- Guide to Renting</li><li>- Lease Appraisal</li><li>- Property Management Team</li><li>- Leased Properties</li><li>- Property Alert</li></ul></div>
</footer>
<div class="abs bottombar">
  <span style="position:absolute;left:60px;top:10px">© 2021 Harborkey Estate Agents - All Right Reserved.</span>
  <div class="social" style="left:1090px;top:6px"><span></span><span></span></div>
</div>

</body>
</html>
```